Gym Wall Story Feature-- Long Horizontal design for the full-width of the gym wall

We need a horizontal, LONG, story poster/display that artfully tells our gym's story using ALL of the attached information and photographs. I've also included where this display will go in our gym (aligned with, and under the trophies.) Please incorporate the color scheme of white, light grey, dark grey, and orange.

Thanks!

Target Market(s)

Upscale, exclusive, hip gym community

Industry/Entity Type

Gym

Font styles to use
Sans Serif

Colors
ffffff
000000
aaaaaa
5c5c5c
f78f20
e9e9e9

Requirements
Must have
• All images and text provided in the attachments. Clean, modern, design. MOSTLY white with just a couple pops of orange and light grey. text should be black or charcoal and easy to read. We would like to have our logo incorporated as well.
Nice to have
• Clean, stream-line look, nothing too busy or crowded.
Should not have
• Too busy, slanted lines, weird fonts, misalignment.

```html
<!DOCTYPE html>
<html lang="en">
<head>
<meta charset="utf-8">
<title>How Did The Forge Start?</title>
<link href="https://fonts.googleapis.com/css2?family=Lato:wght@300;400;700;900&display=swap" rel="stylesheet">
<style>
  :root {
    --white: #ffffff;
    --black: #000000;
    --grey-mid: #aaaaaa;
    --charcoal: #5c5c5c;
    --orange: #f78f20;
    --grey-light: #e9e9e9;
    --ink: #3d3d3d;
  }
  * { margin: 0; padding: 0; box-sizing: border-box; }
  html, body { width: 1200px; height: 724px; overflow: hidden; background: var(--white); }
  .poster {
    position: relative; width: 1200px; height: 724px; overflow: hidden;
    font-family: 'Lato', sans-serif; color: var(--charcoal); background: var(--white);
  }
  .backdrop {
    position: absolute; inset: 0;
    background:
      radial-gradient(ellipse 220px 360px at 90px 380px, var(--grey-light) 0%, rgba(233,233,233,0) 100%),
      radial-gradient(ellipse 260px 300px at 420px 200px, #efefef 0%, rgba(239,239,239,0) 100%),
      radial-gradient(ellipse 240px 340px at 1120px 330px, var(--grey-light) 0%, rgba(233,233,233,0) 100%),
      radial-gradient(ellipse 300px 240px at 800px 250px, #f1f1f1 0%, rgba(241,241,241,0) 100%);
  }
  .photo { position: absolute; }
  .photo--early { left: 124px; top: 112px; width: 98px; height: 157px; background: linear-gradient(160deg, #9a9a9a, #222); }
  .photo--comeback { left: 449px; top: 112px; width: 91px; height: 147px; background: linear-gradient(160deg, #c9a58a, #8a3e22 60%, #3b2a25); }
  .photo--today { left: 767px; top: 112px; width: 103px; height: 154px; background: linear-gradient(160deg, #b8a87a, #4a4a40 60%, #1e1e1e); }

  .story {
    position: absolute; font-size: 11.2px; line-height: 14.7px; font-weight: 300; color: var(--ink);
  }
  .story p + p { margin-top: 14px; }
  .story strong { font-weight: 700; }
  .story--early { left: 234px; top: 111px; width: 184px; }
  .story--comeback { left: 576px; top: 111px; width: 150px; }
  .story--today { left: 878px; top: 111px; width: 184px; }

  .titles-list { list-style: none; position: absolute; left: 879px; top: 261px; }
  .title-row {
    display: flex; width: 169px; height: 20px; margin-bottom: 10px;
    font-size: 7px; color: var(--ink);
  }
  .title-row__year { width: 43px; background: var(--orange); display: flex; align-items: center; justify-content: center; }
  .title-row__name { flex: 1; border: 1px solid var(--grey-mid); background: var(--white); display: flex; align-items: center; justify-content: center; }

  .timeline { position: absolute; left: 0; top: 0; }
  .year { position: absolute; top: 436px; font-size: 16px; font-weight: 700; color: var(--orange); }
  .year--1973 { left: 95px; }
  .year--1981 { left: 416px; }
  .year--2015 { left: 738px; }

  .headline {
    position: absolute; left: 69px; top: 481px; font-size: 41px; line-height: 52px;
    text-transform: uppercase; letter-spacing: 0.3px;
  }
  .headline__accent { color: var(--orange); font-weight: 700; }
  .headline__dark { color: var(--ink); font-weight: 700; }
  .headline__light { color: var(--orange); font-weight: 300; }

  .activity-strip {
    position: absolute; left: 552px; top: 474px; width: 164px; height: 25px;
    background: linear-gradient(90deg, rgba(80,80,80,0), rgba(80,80,80,0.35) 15%, rgba(80,80,80,0.35) 85%, rgba(80,80,80,0));
  }
  .quote-tail { position: absolute; left: 0; top: 0; }
  .quote {
    position: absolute; left: 467px; top: 498px; width: 251px; height: 98px;
    background: var(--orange); color: var(--white); font-weight: 300;
    font-size: 12px; line-height: 15.5px; text-align: center;
    display: flex; align-items: center; justify-content: center; padding: 0 44px;
    box-shadow: 0 2px 6px rgba(0,0,0,0.15);
  }

  .wordmark { position: absolute; left: 0; top: 0; text-transform: uppercase; line-height: 1; }
  .wm { position: absolute; white-space: nowrap; }
  .wm--1981 { left: 821px; top: 476px; font-size: 60px; font-weight: 700; color: var(--charcoal); }
  .wm--mr { left: 944px; top: 502px; font-size: 25px; font-weight: 400; color: var(--charcoal); }
  .wm--1973 { left: 996px; top: 478px; font-size: 31px; font-weight: 400; color: var(--charcoal); }
  .wm--first { left: 825px; top: 524px; font-size: 35px; font-weight: 900; color: var(--orange); }
  .wm--last { left: 856px; top: 553px; font-size: 35px; font-weight: 900; color: var(--orange); }
  .wm--won { left: 1000px; top: 530px; font-size: 17px; font-weight: 300; color: var(--charcoal); }
  .wm--won2 { left: 1000px; top: 545px; font-size: 17px; font-weight: 300; color: var(--charcoal); }
  .wm--2015 { left: 967px; top: 553px; font-size: 56px; font-weight: 700; color: var(--charcoal); }
</style>
</head>
<body>
<main class="poster">
  <div class="backdrop" role="img" aria-label="Faint light grey silhouettes of athletes training"></div>

  <svg class="timeline" width="1200" height="724" aria-hidden="true">
    <line x1="67" y1="421" x2="1132" y2="421" stroke="#333" stroke-width="1"/>
    <polyline points="124,146 117,146 117,421" fill="none" stroke="#555" stroke-width="1"/>
    <polyline points="449,146 439,146 439,421" fill="none" stroke="#555" stroke-width="1"/>
    <polyline points="767,146 760,146 760,421" fill="none" stroke="#555" stroke-width="1"/>
    <g fill="#333">
      <circle cx="141" cy="421" r="2"/><circle cx="168" cy="421" r="2"/><circle cx="195" cy="421" r="2"/>
      <circle cx="222" cy="421" r="2"/><circle cx="248" cy="421" r="2"/><circle cx="275" cy="421" r="2"/>
      <circle cx="302" cy="421" r="2"/><circle cx="328" cy="421" r="2"/><circle cx="355" cy="421" r="2"/>
      <circle cx="382" cy="421" r="2"/><circle cx="409" cy="421" r="2"/>
      <circle cx="463" cy="421" r="2"/><circle cx="489" cy="421" r="2"/><circle cx="516" cy="421" r="2"/>
      <circle cx="543" cy="421" r="2"/><circle cx="570" cy="421" r="2"/><circle cx="596" cy="421" r="2"/>
      <circle cx="623" cy="421" r="2"/><circle cx="650" cy="421" r="2"/><circle cx="676" cy="421" r="2"/>
      <circle cx="703" cy="421" r="2"/><circle cx="730" cy="421" r="2"/>
      <circle cx="787" cy="421" r="2"/><circle cx="813" cy="421" r="2"/><circle cx="840" cy="421" r="2"/>
      <circle cx="867" cy="421" r="2"/><circle cx="893" cy="421" r="2"/><circle cx="920" cy="421" r="2"/>
      <circle cx="947" cy="421" r="2"/><circle cx="974" cy="421" r="2"/><circle cx="1000" cy="421" r="2"/>
      <circle cx="1028" cy="421" r="2"/><circle cx="1055" cy="421" r="2"/>
      <circle cx="117" cy="421" r="7"/><circle cx="439" cy="421" r="7"/><circle cx="760" cy="421" r="7"/>
    </g>
  </svg>

  <div class="photo photo--early" role="img" aria-label="Black and white photo of the young bodybuilder on stage"></div>
  <div class="photo photo--comeback" role="img" aria-label="Colour photo of the bodybuilder posing at his comeback"></div>
  <div class="photo photo--today" role="img" aria-label="Photo of the founder standing in the gym beside dumbbell racks"></div>

  <section class="story story--early">
    <p>The Forge began with body builder and personal trainer, Everett Lowe. Everett had a passion for fitness early on and opened his first gym in 1962.</p>
    <p><strong>Shortly after, Everett won Mr. Pinecrest.</strong></p>
    <p>Everett’s body-building career looked promising until one evening a serious accident left him badly hurt. As a result, Everett suffered from nerve damage in the arm and figured at the age of 34, his weight lifting days were over.</p>
  </section>

  <section class="story story--comeback">
    <p>Everett started with 2-pound weights and changed his whole training technique.</p>
    <p>No more bouncing or slinging, just steady and controlled movements. Through hard work and consistency, Everett started shaping up his upper-body again.</p>
    <p><strong>Shortly after turning 40, Everett won the National Mr. Summit competition.</strong></p>
  </section>

  <section class="story story--today">
    <p>Through his experiences, Everett created The Forge; a system that helps individuals develop a fundamentally sound workout regimen and accountability system.</p>
    <p><strong>National Championships Won:</strong></p>
  </section>

  <ul class="titles-list">
    <li class="title-row"><span class="title-row__year">1981</span><span class="title-row__name">Won Past 40 Mr. Summit</span></li>
    <li class="title-row"><span class="title-row__year">1999</span><span class="title-row__name">Won Past 60 Mr. Summit</span></li>
    <li class="title-row"><span class="title-row__year">1996</span><span class="title-row__name">Won Past 50 Mr. Summit</span></li>
    <li class="title-row"><span class="title-row__year">2009</span><span class="title-row__name">Won Past 70 Mr. Summit</span></li>
  </ul>

  <span class="year year--1973">1973</span>
  <span class="year year--1981">1981</span>
  <span class="year year--2015">2015</span>

  <h1 class="headline">
    <span class="headline__accent">How</span> <span class="headline__dark">did the</span><br>
    <span class="headline__light">Forge</span><span class="headline__dark">Start?</span>
  </h1>

  <div class="activity-strip" role="img" aria-label="Small dark figures doing cycling, push-ups, pull-ups, squats and running"></div>
  <svg class="quote-tail" width="1200" height="724" aria-hidden="true">
    <polygon points="476,444 477,499 530,499" fill="#f78f20"/>
  </svg>
  <blockquote class="quote">“I thought I was through and couldn’t continue lifting but the forge changed everything.”</blockquote>

  <div class="wordmark" aria-label="Everett Lowe, 1973 to 2015">
    <span class="wm wm--1981">1981</span>
    <span class="wm wm--mr">Mr. Summit</span>
    <span class="wm wm--1973">1973</span>
    <span class="wm wm--first">Everett</span>
    <span class="wm wm--last">Lowe</span>
    <span class="wm wm--won">Won Past 70</span>
    <span class="wm wm--won2">Mr. Summit</span>
    <span class="wm wm--2015">2015</span>
  </div>
</main>
</body>
</html>
```